Book Cover Design

Design with title UNWAVERING
Subtitle: Ways to Kindle the Spark of Resolve
Author Name: Carla Jean Morrow
Put DAILY MERIDIAN BESTSELLER at top
Shimmer design, see inspirational images attached

```html
<!DOCTYPE html>
<html lang="en">
<head>
<meta charset="utf-8">
<title>Unwavering — Book Cover</title>
<link rel="stylesheet" href="https://fonts.googleapis.com/css2?family=Arimo:wght@400;700&family=Bebas+Neue&display=swap">
<style>
  :root {
    --ink: #0b0b0d;
    --lavender: #c9b6e6;
    --lilac: #b9a4dc;
    --pink: #ecc9e2;
    --sky: #b8e0f0;
    --aqua: #a9e3ea;
    --pearl: #f6f3fb;
    --ghost: rgba(255, 255, 255, 0.55);
  }
  * { margin: 0; padding: 0; box-sizing: border-box; }
  html, body { width: 1200px; height: 818px; overflow: hidden; background: #fff; }
  .wrap-cover { position: relative; width: 1200px; height: 818px; overflow: hidden; }

  .shimmer {
    position: absolute; inset: 0;
    background:
      radial-gradient(ellipse 260px 90px at 160px 330px, rgba(255,255,255,0.85), transparent 70%),
      radial-gradient(ellipse 300px 80px at 980px 300px, rgba(255,255,255,0.8), transparent 70%),
      radial-gradient(ellipse 260px 120px at 60px 620px, var(--aqua), transparent 70%),
      radial-gradient(ellipse 280px 120px at 420px 120px, var(--pink), transparent 70%),
      radial-gradient(ellipse 320px 160px at 1050px 520px, var(--pearl), transparent 70%),
      radial-gradient(ellipse 300px 160px at 760px 160px, var(--lavender), transparent 70%),
      linear-gradient(160deg, var(--lilac) 0%, var(--pink) 22%, var(--sky) 45%, var(--pearl) 60%, var(--lavender) 80%, var(--pearl) 100%);
  }

  .spine {
    position: absolute; left: 545px; top: 0; width: 115px; height: 818px;
    background: linear-gradient(180deg, var(--pink) 0%, var(--sky) 25%, var(--lavender) 45%, var(--aqua) 65%, var(--pearl) 80%, var(--lilac) 100%);
  }
  .spine-title {
    position: absolute; left: 50%; top: 50%;
    transform: translate(-50%, -50%) rotate(-90deg);
    font-family: "Bebas Neue", sans-serif; font-size: 54px; color: var(--ink);
    letter-spacing: 31px; white-space: nowrap; margin-top: 40px;
  }

  .back, .front { position: absolute; top: 0; height: 818px; overflow: hidden; }
  .back { left: 0; width: 545px; }
  .front { left: 660px; width: 540px; }

  .back-subtitle {
    position: absolute; left: 0; width: 545px; top: 36px; text-align: center;
    font-family: "Arimo", sans-serif; font-weight: 700; color: var(--ink); line-height: 1;
  }
  .back-subtitle .lead { display: block; font-size: 33px; }
  .back-subtitle .main { display: block; font-size: 44px; margin-top: 6px; }

  .bestseller {
    position: absolute; left: 0; width: 540px; top: 17px; text-align: center;
    font-family: "Arimo", sans-serif; font-size: 18px; color: var(--ink);
  }
  .title {
    position: absolute; left: 0; width: 540px; top: 68px; text-align: center;
    font-family: "Bebas Neue", sans-serif; font-size: 128px; line-height: 1; color: var(--ink);
  }
  .subtitle {
    position: absolute; left: 0; width: 540px; top: 206px; text-align: center;
    font-family: "Arimo", sans-serif; font-weight: 700; color: var(--ink); line-height: 1;
  }
  .subtitle .sm { display: block; font-size: 30px; }
  .subtitle .lg { display: block; font-size: 46px; }
  .author {
    position: absolute; left: 0; width: 540px; top: 738px; text-align: center;
    font-family: "Bebas Neue", sans-serif; font-size: 34px; color: var(--ink); letter-spacing: 1px;
  }

  .echo { position: absolute; font-family: "Bebas Neue", sans-serif; color: var(--ghost); white-space: nowrap; line-height: 1; }
  .echo.up { writing-mode: vertical-rl; transform: rotate(180deg); }
</style>
</head>
<body>
<main class="wrap-cover">
  <div class="shimmer" role="img" aria-label="Iridescent holographic shimmer texture in lavender, pink and pale blue"></div>

  <section class="back">
    <h2 class="back-subtitle"><span class="lead">WAYS TO KINDLE THE</span><span class="main">SPARK OF RESOLVE</span></h2>
    <div class="word-cloud" aria-hidden="true">
      <span class="echo up" style="left:200px; top:255px; font-size:44px;">UNWAVERING</span>
      <span class="echo up" style="left:250px; top:300px; font-size:30px;">UNWAVERING</span>
      <span class="echo" style="left:290px; top:408px; font-size:38px;">UNWAVERING</span>
      <span class="echo" style="left:64px; top:460px; font-size:36px;">UNWAVERING</span>
      <span class="echo" style="left:250px; top:455px; font-size:44px;">UNWAVERING</span>
      <span class="echo" style="left:110px; top:503px; font-size:80px;">UNWAVERING</span>
      <span class="echo" style="left:222px; top:588px; font-size:25px;">UNWAVERING</span>
      <span class="echo" style="left:190px; top:622px; font-size:34px;">UNWAVERING</span>
      <span class="echo" style="left:258px; top:666px; font-size:17px;">UNWAVERING</span>
      <span class="echo up" style="left:332px; top:560px; font-size:44px;">UNWAVERING</span>
      <span class="echo up" style="left:390px; top:585px; font-size:19px;">UNWAVERING</span>
    </div>
  </section>

  <aside class="spine">
    <span class="spine-title">UNWAVERING</span>
  </aside>

  <section class="front">
    <p class="bestseller">DAILY MERIDIAN BESTSELLER</p>
    <h1 class="title">UNWAVERING</h1>
    <h2 class="subtitle">
      <span class="sm">WAYS TO</span><span class="lg">KINDLE</span>
      <span class="sm">THE</span><span class="lg">SPARK</span>
      <span class="sm">OF</span><span class="lg">RESOLVE</span>
    </h2>
    <div class="word-cloud" aria-hidden="true">
      <span class="echo up" style="left:406px; top:448px; font-size:36px;">UNWAVERING</span>
      <span class="echo up" style="left:438px; top:412px; font-size:32px;">UNWAVERING</span>
      <span class="echo up" style="left:470px; top:486px; font-size:14px;">UNWAVERING</span>
      <span class="echo" style="left:320px; top:550px; font-size:24px;">UNWAVERING</span>
      <span class="echo" style="left:445px; top:548px; font-size:36px;">UNWAVERING</span>
      <span class="echo" style="left:345px; top:575px; font-size:50px;">UNWAVERING</span>
      <span class="echo" style="left:347px; top:632px; font-size:16px;">UNWAVERING</span>
      <span class="echo" style="left:337px; top:655px; font-size:25px;">UNWAVERING</span>
      <span class="echo" style="left:360px; top:682px; font-size:11px;">UNWAVERING</span>
      <span class="echo up" style="left:512px; top:610px; font-size:30px;">UNWAVERING</span>
    </div>
    <p class="author">CARLA JEAN MORROW</p>
  </section>
</main>
</body>
</html>
```